Design Back of Business Cards with design concept provided

1. Change the color scheme to match the current business card
2. Change orientation to landscape (Rectangle w/o rounded corners. Match the size of the business card attached)
3. Change "Mark your order" to "Our services"
4. Change the picture of the car to a house/property. Or maybe remove it altogether depending on what looks better
5. Change the menu & description to
- Property Agent: We help you sell, buy and lease properties. Selling and buying properties can be intimidating and time consuming. We'll guide you through the process.
- Home Handyman: We do all types of work around the house. Renovation, repairs, maintenance, painting, plastering, tiling, roofing, locks, doors, windows, ceiling and much more
- Property Project Management: If you own a land, and looking to make money from it, we can develop it for you into a profitable property project
- Property Investment: Investing in properties have always provided an above average return. We can put your money into a sound, yet high-return property projects

```html
<!DOCTYPE html>
<html lang="en">
<head>
<meta charset="utf-8">
<title>Sarantara Real Estate – Business Cards</title>
<link href="https://fonts.googleapis.com/css2?family=Open+Sans:wght@400;600;700;800&family=Oswald:wght@600&display=swap" rel="stylesheet">
<style>
  :root {
    --brown: #4d3a37;
    --orange: #f27f22;
    --white: #ffffff;
    --ground: #e9e6e2;
    --card-w: 700px;
    --card-h: 400px;
  }
  * { box-sizing: border-box; margin: 0; padding: 0; }
  html, body { width: 1200px; height: 900px; overflow: hidden; }
  body {
    background: var(--ground);
    font-family: "Open Sans", Arial, sans-serif;
    display: flex; flex-direction: column; align-items: center;
    gap: 40px; padding-top: 30px;
  }
  .card {
    position: relative; width: var(--card-w); height: var(--card-h);
    background: var(--brown); overflow: hidden;
    box-shadow: 0 6px 18px rgba(0,0,0,.18);
  }
  .wordmark { font-weight: 800; letter-spacing: -1px; line-height: 1; }
  .tagline { font-weight: 700; letter-spacing: 3px; line-height: 1; }

  /* ---------- back: services ---------- */
  .back .white-band { position: absolute; left: 0; right: 0; top: 44px; height: 116px; background: var(--white); }
  .back .houses-art {
    position: absolute; right: 36px; top: 12px; width: 120px; height: 52px;
    background: linear-gradient(90deg, var(--brown) 0%, var(--orange) 50%, var(--brown) 100%);
  }
  .back .brand { position: absolute; right: 168px; top: 60px; text-align: right; }
  .back .brand .wordmark { color: var(--brown); font-size: 42px; }
  .back .brand .tagline { color: var(--orange); font-size: 13px; margin-top: 2px; }
  .back .services-title {
    position: absolute; left: 36px; top: 118px;
    font-family: "Oswald", "Arial Narrow", sans-serif; font-weight: 600;
    font-size: 30px; color: var(--brown); letter-spacing: .5px;
  }
  .back .services { position: absolute; left: 0; right: 0; top: 160px; height: 210px; background: var(--orange); list-style: none; }
  .service {
    position: relative; height: 52.5px; display: flex; align-items: center;
    border-bottom: 1px dashed rgba(255,255,255,.8); padding: 0 30px 0 36px;
  }
  .service:last-child { border-bottom: none; }
  .service::before {
    content: ""; position: absolute; left: -10px; top: 50%; width: 24px; height: 14px;
    margin-top: -7px; background: var(--white); border-radius: 5px;
  }
  .service-name { width: 170px; flex: none; color: var(--white); font-weight: 800; font-size: 13px; line-height: 1.1; text-transform: uppercase; }
  .service-desc { color: var(--white); font-size: 10.5px; line-height: 1.35; }

  /* ---------- front: contact ---------- */
  .front .orange-band { position: absolute; left: 0; right: 0; top: 104px; height: 150px; background: var(--orange); }
  .front .brand { position: absolute; left: 110px; top: 142px; }
  .front .brand .wordmark { color: var(--white); font-size: 58px; }
  .front .brand .tagline { color: var(--brown); font-size: 18px; margin: 4px 0 0 96px; }
  .contacts { position: absolute; left: 470px; top: 128px; list-style: none; color: var(--white); font-size: 11px; line-height: 1.3; }
  .contacts li { display: flex; align-items: flex-start; gap: 6px; margin-bottom: 2px; }
  .contacts svg { flex: none; margin-top: 2px; }
  .name-band { position: absolute; left: 0; right: 0; top: 300px; height: 60px; background: var(--orange); }
  .name-tab { position: absolute; left: -16px; top: 286px; width: 70px; height: 88px; background: var(--white); border-radius: 14px; }
  .person-name { position: absolute; left: 78px; top: 316px; color: var(--white); font-size: 20px; font-weight: 400; }
</style>
</head>
<body>

<section class="card back" aria-label="Card back – our services">
  <div class="white-band"></div>
  <div class="houses-art" role="img" aria-label="Illustration of a row of small house silhouettes"></div>
  <div class="brand">
    <div class="wordmark">Sarantara</div>
    <div class="tagline">REAL ESTATE</div>
  </div>
  <h2 class="services-title">OUR SERVICES</h2>
  <ul class="services">
    <li class="service"><span class="service-name">Property<br>Agent:</span><span class="service-desc">We help you sell, buy and lease properties. Selling and buying properties can be intimidating and time consuming. We'll guide you through the process.</span></li>
    <li class="service"><span class="service-name">Home<br>Handyman:</span><span class="service-desc">We do all types of work around the house. Renovation, repairs, maintenance, painting, plastering, tiling, roofing, locks, doors, windows, ceiling and much more.</span></li>
    <li class="service"><span class="service-name">Property Project<br>Management:</span><span class="service-desc">If you own a land, and looking to make money from it, we can develop it for you into a profitable property project.</span></li>
    <li class="service"><span class="service-name">Property<br>Investment:</span><span class="service-desc">Investing in properties have always provided an above average return. We can put your money into a sound, yet high-return property projects.</span></li>
  </ul>
</section>

<section class="card front" aria-label="Card front – contact">
  <div class="orange-band"></div>
  <div class="brand">
    <div class="wordmark">Sarantara</div>
    <div class="tagline">REAL ESTATE</div>
  </div>
  <ul class="contacts">
    <li>
      <svg width="11" height="11" viewBox="0 0 12 12" aria-hidden="true"><circle cx="6" cy="6" r="6" fill="#fff"/><path d="M6 2.5a2 2 0 0 0-2 2c0 1.5 2 4 2 4s2-2.5 2-4a2 2 0 0 0-2-2z" fill="#f27f22"/></svg>
      <span>Menara Kirana Tower II, 6th Floor<br>Jl. Cempaka Raya No. 27<br>Jakarta Selatan 12740</span>
    </li>
    <li>
      <svg width="11" height="11" viewBox="0 0 12 12" aria-hidden="true"><circle cx="6" cy="6" r="6" fill="#fff"/><path d="M4 3l1.2 1.4-.6.8c.5 1 1.2 1.7 2.2 2.2l.8-.6L9 8l-.8 1C6 9 3 6 3 3.8z" fill="#f27f22"/></svg>
      <span>+62 21 5550 1842</span>
    </li>
    <li>
      <svg width="11" height="11" viewBox="0 0 12 12" aria-hidden="true"><circle cx="6" cy="6" r="6" fill="#fff"/><rect x="4.2" y="2.6" width="3.6" height="6.8" rx=".8" fill="#f27f22"/></svg>
      <span>+62 815 5501 9344</span>
    </li>
    <li>
      <svg width="11" height="11" viewBox="0 0 12 12" aria-hidden="true"><circle cx="6" cy="6" r="6" fill="#fff"/><rect x="3" y="4" width="6" height="4.2" fill="#f27f22"/><path d="M3 4l3 2.4L9 4" stroke="#fff" stroke-width=".7" fill="none"/></svg>
      <span>dion@sarantara.com</span>
    </li>
    <li>
      <svg width="11" height="11" viewBox="0 0 12 12" aria-hidden="true"><circle cx="6" cy="6" r="6" fill="#fff"/><circle cx="6" cy="6" r="3" fill="none" stroke="#f27f22" stroke-width=".9"/><path d="M3 6h6M6 3v6" stroke="#f27f22" stroke-width=".7"/></svg>
      <span>www.sarantara.com</span>
    </li>
  </ul>
  <div class="name-band"></div>
  <div class="name-tab"></div>
  <p class="person-name">Dion Sarantara</p>
</section>

</body>
</html>
```